Brand Business Card for Hotel Cloud Management System

Hello designers,
we are looking for a new brand business card for our product Stayvora. Our brand Stayvora is a hotel management system for small hotels, B&B, guesthouses etc. and just recently we are expanding our offer to other European markets. Therefore we need a business card that will communicate not only to the end-users (hoteliers) but also to potential business partners/ We would like the brand business card to be professional looking, but not too serius, modern, elegant, clean, Our brand color is orange, dark grey and it would be nice to see both combined.

Please visit our website www.stayvora.eu to get more impression on what our brand stayvora stands for.

Please find attached stayvora logo.

Target Market(s)

small hotels, hoteliers, B&B owners, potential business partners

Industry/Entity Type

Software Service

Contact Information for Business Card

Stayvora
- hotel software solutions - web booking engine - multi channel manager
www.stayvora.eu
T: +38614738265
E: info@stayvora.net

Font styles to use
Serif
Sans Serif

Colors
f37122
aaaaaa
606060
f6f6f6

Requirements
Must have
• Logo of the brand
• the layout of the business card should be in connection with the look and feel of the website stayvora.eu and logo stayvora;

```html
<!DOCTYPE html>
<html lang="en">
<head>
<meta charset="utf-8">
<title>Stayvora Business Card</title>
<link rel="stylesheet" href="https://fonts.googleapis.com/css2?family=Lato:wght@400;700;900&display=swap">
<style>
  :root {
    --brand-orange: #f37122;
    --brand-dark: #3a3a3a;
    --brand-grey: #606060;
    --brand-light: #f6f6f6;
    --stripe-dark: #2b2521;
    --page-bg: #e4e4e4;
    --ink: #111111;
  }
  * { margin: 0; padding: 0; box-sizing: border-box; }
  html, body {
    width: 1200px;
    height: 970px;
    overflow: hidden;
    background: var(--page-bg);
    font-family: "Lato", sans-serif;
  }
  .business-card {
    position: absolute;
    left: 100px;
    top: 185px;
    width: 1000px;
    height: 600px;
    display: flex;
    box-shadow: 0 10px 30px rgba(0, 0, 0, 0.18);
  }
  .card-front {
    position: relative;
    width: 486px;
    height: 100%;
    background: var(--brand-light);
  }
  .brand-block {
    position: absolute;
    top: 270px;
    left: 0;
    width: 100%;
    text-align: center;
  }
  .brand-name {
    font-weight: 900;
    font-size: 72px;
    letter-spacing: -1px;
    line-height: 1;
    color: var(--brand-dark);
  }
  .brand-tagline {
    margin-top: 12px;
    font-size: 27px;
    font-weight: 400;
    color: var(--brand-grey);
  }
  .service-list {
    position: absolute;
    left: 100px;
    top: 452px;
    list-style: none;
  }
  .service-item {
    display: flex;
    align-items: center;
    gap: 10px;
    height: 37px;
    font-size: 21px;
    color: var(--brand-grey);
  }
  .service-bullet {
    width: 10px;
    height: 10px;
    background: var(--brand-orange);
  }
  .card-divider {
    position: relative;
    width: 31px;
    height: 100%;
    background: var(--brand-orange);
  }
  .divider-line {
    position: absolute;
    top: 0;
    width: 7px;
    height: 100%;
    background: var(--stripe-dark);
  }
  .divider-line--first { left: 4px; }
  .divider-line--second { left: 20px; }
  .card-back {
    position: relative;
    flex: 1;
    height: 100%;
    background: var(--brand-orange);
  }
  .contact-list {
    position: absolute;
    left: 109px;
    top: 233px;
    list-style: none;
  }
  .contact-item {
    display: flex;
    align-items: center;
    gap: 16px;
    height: 56px;
    font-size: 26px;
    color: var(--ink);
  }
  .contact-icon {
    width: 38px;
    height: 38px;
    flex: none;
  }
  .contact-web {
    margin-top: 6px;
    font-size: 29px;
    font-weight: 900;
    letter-spacing: 0.5px;
    color: var(--ink);
  }
</style>
</head>
<body>
  <div class="business-card">
    <section class="card-front">
      <div class="brand-block">
        <div class="brand-name">Stayvora</div>
        <div class="brand-tagline">hotel pms service</div>
      </div>
      <ul class="service-list">
        <li class="service-item"><span class="service-bullet"></span>Web Booking Engine</li>
        <li class="service-item"><span class="service-bullet"></span>Hotel Software Solutions</li>
        <li class="service-item"><span class="service-bullet"></span>Multi Channel Manager</li>
      </ul>
    </section>

    <div class="card-divider">
      <span class="divider-line divider-line--first"></span>
      <span class="divider-line divider-line--second"></span>
    </div>

    <section class="card-back">
      <ul class="contact-list">
        <li class="contact-item">
          <svg class="contact-icon" viewBox="0 0 38 38" aria-hidden="true">
            <circle cx="19" cy="19" r="19" fill="#111"/>
            <path d="M11 16c0-3 4-5 8-5s8 2 8 5v2h-4v-2c-1-1-7-1-8 0v2h-4z" fill="#fff"/>
            <rect x="12" y="20" width="14" height="8" rx="2" fill="#fff"/>
            <circle cx="19" cy="24" r="2" fill="#111"/>
          </svg>
          <span class="contact-text">+38614738265</span>
        </li>
        <li class="contact-item">
          <svg class="contact-icon" viewBox="0 0 38 38" aria-hidden="true">
            <circle cx="19" cy="19" r="19" fill="#111"/>
            <rect x="10" y="13" width="18" height="12" fill="#fff"/>
            <path d="M10 13l9 7 9-7" fill="none" stroke="#111" stroke-width="1.6"/>
          </svg>
          <span class="contact-text">info@stayvora.net</span>
        </li>
      </ul>
      <div class="contact-list" style="top:356px;left:109px;">
        <div class="contact-web">www.stayvora.eu</div>
      </div>
    </section>
  </div>
</body>
</html>
```